QLN Structural Approval Standards Private Assessors

Professional Construction Consultancy Company Business Card - must keep logo colours see images below - examples have been added from my last competition - please see them as examples only!

Target Market(s)

Home Builders

Industry/Entity Type

Construction

Contact Information for Business Card

See "must haves"

Font styles to use
Sans Serif

Colors
ffffff
add136
000000

Requirements
Must have
• Daniel Moravi
• Director
• Phone: 0431 587 219
• Address: 7 Tarrunga Rd,
• Hallworth Vale, SA, 5091
• Email: qlnassessors@mailbox-example.com
• Website: www.qlnassessors-example.com.au
• Facebook: QLN Structural Approval Standards
Nice to have
• Side 1: full logo
• Side 2: company details
Should not have
• hard to read
• must be clear and professional

```html
<!DOCTYPE html>
<html lang="en">
<head>
<meta charset="utf-8">
<title>QLN Structural Approval Standards – Business Card</title>
<link href="https://fonts.googleapis.com/css2?family=Roboto:wght@400;500;700&display=swap" rel="stylesheet">
<style>
  :root {
    --bg: #d1d2d4;
    --white: #ffffff;
    --green: #add136;
    --black: #000000;
    --ink: #111111;
  }
  * { box-sizing: border-box; margin: 0; padding: 0; }
  html, body { width: 1200px; height: 1200px; overflow: hidden; }
  body {
    background: var(--bg);
    font-family: "Roboto", Arial, sans-serif;
    color: var(--ink);
    position: relative;
  }
  .card {
    position: absolute;
    left: 303px;
    width: 593px;
    height: 333px;
    background: var(--white);
    border-radius: 26px;
    overflow: hidden;
  }
  .card--front { top: 170px; }
  .card--back { top: 640px; }

  .card__stripe {
    position: absolute; left: 0; right: 0; bottom: 33px;
    height: 5px; background: var(--green);
  }
  .card__footer {
    position: absolute; left: 0; right: 0; bottom: 0;
    height: 33px; background: var(--black);
    display: flex; align-items: center; justify-content: center;
  }
  .card__website {
    color: var(--white); font-size: 11.5px; letter-spacing: 1.4px; font-weight: 400;
  }

  /* company name lockup */
  .brand { display: flex; align-items: center; }
  .brand__mark { background: var(--green); flex: none; }
  .brand__name { font-weight: 700; color: var(--black); text-transform: uppercase; line-height: 1.2; white-space: nowrap; }

  .card--front .brand {
    position: absolute; left: 0; right: 0; top: 128px; justify-content: center; gap: 12px;
  }
  .card--front .brand__mark { width: 56px; height: 56px; }
  .card--front .brand__name { font-size: 16px; letter-spacing: 1.2px; }

  .card--back .brand { position: absolute; left: 62px; top: 46px; gap: 7px; }
  .card--back .brand__mark { width: 28px; height: 28px; }
  .card--back .brand__name { font-size: 7.5px; letter-spacing: .6px; }

  .person { position: absolute; left: 61px; top: 162px; }
  .person__name { color: var(--green); font-weight: 700; font-size: 24px; letter-spacing: -.2px; }
  .person__role { font-size: 11px; letter-spacing: 1px; margin-top: 6px; }

  .contact { position: absolute; left: 325px; top: 164px; font-size: 10.5px; letter-spacing: .9px; }
  .contact__address { line-height: 19px; margin-bottom: 14px; }
  .contact__list { list-style: none; }
  .contact__item { display: flex; align-items: center; height: 19px; }
  .contact__icon { width: 11px; height: 11px; margin-right: 13px; flex: none; }
</style>
</head>
<body>

  <section class="card card--front" aria-label="Business card front">
    <div class="brand">
      <span class="brand__mark"></span>
      <span class="brand__name">QLN Structural Approval Standards<br>Private Assessors</span>
    </div>
    <div class="card__stripe"></div>
    <div class="card__footer"><span class="card__website">www.qlnassessors-example.com.au</span></div>
  </section>

  <section class="card card--back" aria-label="Business card back">
    <div class="brand">
      <span class="brand__mark"></span>
      <span class="brand__name">QLN Structural Approval Standards<br>Private Assessors</span>
    </div>

    <div class="person">
      <p class="person__name">Daniel Moravi</p>
      <p class="person__role">director</p>
    </div>

    <div class="contact">
      <p class="contact__address">7 Tarrunga Rd,<br>Hallworth Vale, SA, 5091</p>
      <ul class="contact__list">
        <li class="contact__item">
          <svg class="contact__icon" viewBox="0 0 11 11" aria-hidden="true"><rect x="2.5" y="0.8" width="6" height="9.4" rx="1" fill="none" stroke="#add136" stroke-width="1.4"/><rect x="4.5" y="8" width="2" height="1" fill="#add136"/></svg>
          0431 587 219
        </li>
        <li class="contact__item">
          <svg class="contact__icon" viewBox="0 0 11 11" aria-hidden="true"><rect x="0.7" y="2" width="9.6" height="7" fill="none" stroke="#add136" stroke-width="1.2"/><path d="M1 2.5 L5.5 6 L10 2.5" fill="none" stroke="#add136" stroke-width="1.2"/></svg>
          qlnassessors@mailbox-example.com
        </li>
        <li class="contact__item">
          <svg class="contact__icon" viewBox="0 0 11 11" aria-hidden="true"><rect x="0.5" y="0.5" width="10" height="10" rx="1" fill="#add136"/></svg>
          QLN Structural Approval Standards
        </li>
      </ul>
    </div>

    <div class="card__stripe"></div>
    <div class="card__footer"><span class="card__website">www.qlnassessors-example.com.au</span></div>
  </section>

</body>
</html>
```